Business Card needed for Drainor, a growing Septic Service company

Drainor, a growing local septic service company in Pennsylvania, needs updated business cards. We'd like the business card to feature our logo and communicate that we provide Septic Pumping, Installations/Repairs, Restroom Rentals, and 24/7 Emergency Service. The business card should be eye-catching, bold, and clean/simple. We have been in business almost 10 years and would like to expand and update our business brand and image.

Target Market(s)

Residential and Commercial, New and Current Homeowners

Industry/Entity Type

Service

Contact Information for Business Card

Contact on the business card should be: Dean Harlow Owner & Operator
Phone: 610-555-0187
Email: service@drainor-example.com
Website: www.drainor-example.com
Address: 812 Millbrook Lane Brookvale PA 18999

Font styles to use
Sans Serif

Colors

Designer to choose colors to be used in the design.

Requirements
Must have
• Feature logo on both side of business card.
Nice to have
• We envision the contact information on one side and our services listed on the other side. Utilize the green from the symbol in our logo as part of the design, overall design color scheme should be white, grey, black.

```html
<!DOCTYPE html>
<html lang="en">
<head>
<meta charset="utf-8">
<title>Drainor Business Card</title>
<link href="https://fonts.googleapis.com/css2?family=Open+Sans:wght@300;400;600;700;800&family=Saira+Condensed:wght@700&display=swap" rel="stylesheet">
<style>
  :root {
    --green: #7dc92e;
    --charcoal: #383536;
    --ink: #1a1a1a;
    --body-ink: #2a2a2a;
    --paper: #ffffff;
    --light-text: #e8e8e8;
  }
  * { margin: 0; padding: 0; box-sizing: border-box; }
  html, body { width: 1200px; height: 1200px; overflow: hidden; background: var(--paper); }
  body { position: relative; font-family: "Open Sans", sans-serif; }

  .card {
    position: absolute;
    left: 226px;
    width: 743px;
    height: 426px;
    box-shadow: 0 1px 4px rgba(0,0,0,0.35);
  }
  .card--front { top: 129px; background: var(--paper); }
  .card--back { top: 640px; background: var(--charcoal); }

  .brand {
    position: absolute;
    display: flex;
    align-items: center;
  }
  .brand__square { background: var(--green); flex: none; }
  .brand__name {
    font-family: "Open Sans", sans-serif;
    font-weight: 800;
    text-transform: uppercase;
    line-height: 1;
  }
  .card--front .brand { left: 68px; top: 183px; gap: 12px; }
  .card--front .brand__square { width: 58px; height: 58px; }
  .card--front .brand__name { font-size: 48px; color: var(--ink); letter-spacing: 1px; }
  .card--back .brand { left: 141px; top: 149px; gap: 16px; }
  .card--back .brand__square { width: 87px; height: 87px; }
  .card--back .brand__name { font-size: 74px; color: var(--paper); letter-spacing: 2px; }

  .divider {
    position: absolute;
    left: 422px; top: 120px;
    width: 1.5px; height: 208px;
    background: var(--green);
  }
  .contact { position: absolute; left: 443px; top: 116px; color: var(--ink); white-space: nowrap; }
  .contact__name {
    font-family: "Saira Condensed", sans-serif;
    font-weight: 700;
    font-size: 38px;
    line-height: 1;
    color: var(--green);
    letter-spacing: 0.5px;
  }
  .contact__role { font-size: 14.5px; font-weight: 600; line-height: 1; margin-top: 1px; }
  .contact__address { font-size: 20px; font-weight: 400; line-height: 24px; margin-top: 20px; color: var(--body-ink); }
  .contact__list { list-style: none; margin-top: 14px; }
  .contact__item {
    display: flex; align-items: center; gap: 12px;
    font-size: 18.5px; line-height: 27px; color: var(--body-ink);
    white-space: nowrap;
  }
  .contact__icon { width: 18px; height: 18px; flex: none; }

  .services {
    position: absolute; left: 0; top: 302px; width: 100%;
    list-style: none; color: var(--light-text);
    font-size: 21px; font-weight: 300;
  }
  .services__item { position: absolute; white-space: nowrap; line-height: 1; }
  .services__item::before {
    content: ""; position: absolute; left: -15px; top: 8px;
    width: 9px; height: 9px; border-radius: 50%; background: var(--green);
  }
</style>
</head>
<body>
  <section class="card card--front">
    <div class="brand">
      <span class="brand__square"></span>
      <span class="brand__name">Drainor</span>
    </div>
    <div class="divider"></div>
    <div class="contact">
      <h1 class="contact__name">DEAN HARLOW</h1>
      <p class="contact__role">Owner &amp; Operator</p>
      <p class="contact__address">812 Millbrook Lane<br>Brookvale PA 18999</p>
      <ul class="contact__list">
        <li class="contact__item">
          <svg class="contact__icon" viewBox="0 0 24 24"><path fill="#7dc92e" d="M6.6 10.8a15.1 15.1 0 0 0 6.6 6.6l2.2-2.2a1 1 0 0 1 1-.25 11.4 11.4 0 0 0 3.6.57 1 1 0 0 1 1 1V20a1 1 0 0 1-1 1A17 17 0 0 1 3 4a1 1 0 0 1 1-1h3.5a1 1 0 0 1 1 1c0 1.25.2 2.450.57 3.57a1 1 0 0 1-.25 1z"/></svg>
          610-555-0187
        </li>
        <li class="contact__item">
          <svg class="contact__icon" viewBox="0 0 24 24"><rect x="2" y="5" width="20" height="14" fill="#7dc92e"/><path d="M2 5l10 8 10-8M2 19l8-7M22 19l-8-7" stroke="#fff" stroke-width="1.6" fill="none"/></svg>
          service@drainor-example.com
        </li>
        <li class="contact__item">
          <svg class="contact__icon" viewBox="0 0 24 24"><g fill="none" stroke="#7dc92e" stroke-width="2"><circle cx="12" cy="12" r="10"/><ellipse cx="12" cy="12" rx="4.5" ry="10"/><path d="M2 12h20M4 6.5h16M4 17.5h16"/></g></svg>
          www.drainor-example.com
        </li>
      </ul>
    </div>
  </section>

  <section class="card card--back">
    <div class="brand">
      <span class="brand__square"></span>
      <span class="brand__name">Drainor</span>
    </div>
    <ul class="services">
      <li class="services__item" style="left:93px;top:0">Septic Pumping</li>
      <li class="services__item" style="left:286px;top:0">Installations/Repairs</li>
      <li class="services__item" style="left:518px;top:-1px">Restroom Rentals</li>
      <li class="services__item" style="left:267px;top:32px">24/7 Emergency Service</li>
    </ul>
  </section>
</body>
</html>
```